Business Card Design - Service Company

Use of the card mainly in living rooms and relations b2b We wish a card with a modern design, blue tones in the background would be a plus The card must be front / back (one side with the logo / the other with the information of contact )

Font styles to use
Serif

Requirements
Must have
• Using the map on the back of the business card Editable format! Photoshop CS2 / Illustrator CS2
Nice to have
• Maquis Vertex IT Pierre Blanche Commercial Center, 20480 Lorvanu 0495718243 Siret 71384096200018 APE 6203Y https://www.fb.com/ateliertech.maquisvertex www.maquis-vertex.com

```html
<!DOCTYPE html>
<html lang="en">
<head>
<meta charset="utf-8">
<title>Maquis Vertex IT — Business Card</title>
<link rel="stylesheet" href="https://fonts.googleapis.com/css2?family=Poppins:wght@400;500;600&display=swap">
<style>
  :root {
    --backdrop: #9b9b9b;
    --paper: #f4f4f4;
    --ink: #3a3a3a;
    --ink-soft: #555555;
    --brand-blue: #1f7fcf;
    --navy: #0b1628;
  }
  * { margin: 0; padding: 0; box-sizing: border-box; }
  html, body {
    width: 1200px; height: 720px; overflow: hidden;
    background: var(--backdrop);
    font-family: "Poppins", sans-serif;
  }
  .stage {
    position: relative; width: 1200px; height: 720px;
    display: flex; align-items: center; justify-content: center; gap: 60px;
  }
  .card {
    position: relative; width: 520px; height: 298px;
    border-radius: 3px; overflow: hidden;
    box-shadow: 0 4px 10px rgba(0,0,0,0.25);
  }
  /* Contact side */
  .card--contact { background: var(--paper); color: var(--ink); }
  .holder { position: absolute; left: 78px; top: 34px; text-align: center; }
  .holder__name { font-size: 22px; font-weight: 600; letter-spacing: -0.5px; line-height: 1; }
  .holder__role { font-size: 8px; letter-spacing: 3px; margin-top: 6px; color: var(--ink-soft); }
  .contact-list {
    position: absolute; left: 28px; top: 96px;
    font-size: 10px; line-height: 14px; font-weight: 500;
    letter-spacing: 0.6px; color: var(--ink-soft); list-style: none;
  }
  .contact-list .gap { margin-top: 6px; }
  .brand-mark {
    position: absolute; right: 34px; top: 150px;
    display: flex; align-items: center; gap: 10px;
  }
  .brand-mark__name { font-size: 22px; font-weight: 600; color: var(--brand-blue); letter-spacing: 0.3px; }
  .brand-mark__square { width: 14px; height: 14px; background: var(--brand-blue); }
  .web-band {
    position: absolute; left: 70px; right: -10px; bottom: 0; height: 48px;
    background: var(--brand-blue); border-radius: 24px 24px 0 0;
    display: flex; align-items: center; justify-content: center;
  }
  .web-band__url { color: #ffffff; font-size: 12px; font-weight: 500; letter-spacing: 3px; text-transform: uppercase; }
  /* Logo side */
  .card--logo {
    background: var(--navy);
    display: flex; align-items: center; justify-content: center;
  }
  .card--logo .brand-mark { position: static; }
  .card--logo .brand-mark__name { font-size: 28px; }
  .card--logo .brand-mark__square { width: 18px; height: 18px; }
</style>
</head>
<body>
<main class="stage">
  <section class="card card--logo" aria-label="Card front">
    <div class="brand-mark">
      <span class="brand-mark__name">Maquis Vertex IT</span>
      <span class="brand-mark__square"></span>
    </div>
  </section>

  <section class="card card--contact" aria-label="Card back">
    <div class="holder">
      <p class="holder__name">YOUR NAME</p>
      <p class="holder__role">CREATOR</p>
    </div>
    <ul class="contact-list">
      <li>YOUR OFFICE</li>
      <li>1234 ADDRESS, STREET</li>
      <li>100 CITY, CA 12345</li>
      <li class="gap">PHONE: (123) 345-6789</li>
      <li>EMAIL: MAQUISVIT@MAILBOX.COM</li>
    </ul>
    <div class="brand-mark">
      <span class="brand-mark__name">Maquis Vertex IT</span>
      <span class="brand-mark__square"></span>
    </div>
    <div class="web-band">
      <span class="web-band__url">www.maquisvertexit.com</span>
    </div>
  </section>
</main>
</body>
</html>
```